Unique business card design

We are looking for a design that reflects our unique social media and online marketing agency "Kestrel Media". We are a young agency with a focus on speakers, coaches and trainers. In other words, we support people who want to do good with their work and help other people live a happier, more successful and fulfilling life, reach as many people as possible with their work and thus have an influence. Our values are: sustainability, creating added value, individuality, proactivity. We want our clients to feel comfortable with us and that's why the relationship with them is very important to us. We want every customer to become a lifelong friend of the company. Most of our clients are premium coaches, meaning they are in the higher priced segment and expect seriousness, professionalism and quality. All of these things should reflect our business card as well. I look forward to feedback. Best regards, Tomas Wylander

```html
<!DOCTYPE html>
<html lang="en">
<head>
<meta charset="utf-8">
<title>Kestrel Media – Business Card</title>
<link rel="stylesheet" href="https://fonts.googleapis.com/css2?family=Questrial&family=Montserrat:wght@600;700&display=swap">
<style>
  :root {
    --navy: #0b0a6a;
    --navy-deep: #07064f;
    --blue: #1f6fc6;
    --paper: #f7f7f8;
    --ink-grey: #6e6e74;
    --rule-grey: #9a9ab0;
    --backdrop: #d9d9dc;
  }
  * { box-sizing: border-box; margin: 0; padding: 0; }
  html, body { width: 1200px; height: 799px; overflow: hidden; }
  body {
    background: var(--backdrop);
    font-family: "Questrial", sans-serif;
    position: relative;
  }
  .card {
    position: absolute;
    top: 245px;
    width: 540px;
    height: 309px;
    overflow: hidden;
    box-shadow: 0 6px 18px rgba(0,0,0,.18);
  }
  .card--front { left: 40px; background: var(--paper); }
  .card--back { left: 620px; background: var(--navy); }

  .front-panel { position: absolute; inset: 0; }

  .wordmark {
    font-family: "Questrial", sans-serif;
    font-weight: 400;
    font-size: 34px;
    line-height: 1;
    letter-spacing: .5px;
    display: flex;
    align-items: center;
    gap: 10px;
    white-space: nowrap;
  }
  .wordmark__square { width: 26px; height: 26px; flex: none; }
  .tagline {
    font-size: 12.5px;
    letter-spacing: .6px;
    margin-top: 6px;
    white-space: nowrap;
  }

  .front-brand { position: absolute; left: 30px; top: 34px; color: var(--navy); }
  .front-brand .wordmark { font-size: 28px; gap: 9px; }
  .front-brand .wordmark__square { width: 22px; height: 22px; background: var(--blue); }
  .front-brand .tagline { color: var(--navy); padding-left: 31px; font-size: 11.5px; }

  .contact-list {
    position: absolute;
    left: 30px;
    top: 124px;
    list-style: none;
    color: var(--ink-grey);
    font-size: 13px;
    line-height: 18px;
  }
  .contact-list li { display: flex; align-items: center; gap: 9px; white-space: nowrap; }
  .contact-list svg { width: 11px; height: 11px; fill: var(--navy); flex: none; }

  .address {
    position: absolute;
    left: 110px;
    top: 236px;
    color: var(--ink-grey);
    font-size: 13px;
    line-height: 19px;
    font-style: normal;
    white-space: nowrap;
  }

  .person {
    position: absolute;
    right: 24px;
    top: 224px;
    text-align: right;
    color: #fff;
    font-family: "Montserrat", sans-serif;
    white-space: nowrap;
  }
  .person__name { font-weight: 700; font-size: 15px; letter-spacing: 1px; }
  .person__role { font-weight: 600; font-size: 11px; letter-spacing: 1.3px; margin-top: 3px; }

  .back-brand {
    position: absolute;
    left: 0; right: 0;
    top: 82px;
    display: flex;
    flex-direction: column;
    align-items: center;
    color: #fff;
  }
  .back-brand .wordmark__square { background: var(--blue); }
  .back-brand .tagline { color: #e6e6f2; }

  .social-row {
    position: absolute;
    left: 0; right: 0;
    top: 190px;
    display: flex;
    align-items: center;
    justify-content: center;
    gap: 8px;
  }
  .social-row__rule { width: 110px; height: 1px; background: var(--rule-grey); }
  .social-row__dots { display: flex; gap: 7px; padding: 0 6px; }
  .social-dot { width: 20px; height: 20px; border-radius: 50%; background: var(--rule-grey); }
</style>
</head>
<body>

<section class="card card--front" aria-label="Business card, front">
  <svg class="front-panel" viewBox="0 0 540 309" aria-hidden="true">
    <polygon points="302,0 540,0 540,309 286,309 372,150" fill="var(--navy)"/>
    <polygon points="280,0 292,0 362,150 278,309 266,309 350,150" fill="var(--navy-deep)"/>
  </svg>

  <div class="front-brand">
    <div class="wordmark"><span class="wordmark__square"></span>Kestrel Media</div>
    <div class="tagline">Online Marketing Services</div>
  </div>

  <ul class="contact-list">
    <li><svg viewBox="0 0 12 12"><path d="M2.5 1h2l1 3-1.5 1a6 6 0 0 0 3 3l1-1.5 3 1v2c0 .6-.4 1-1 1A10 10 0 0 1 1.5 2c0-.6.4-1 1-1z"/></svg>415 208 7731</li>
    <li><svg viewBox="0 0 12 12"><rect x="3" y="0.5" width="6" height="11" rx="1"/></svg>415 208 7732</li>
    <li><svg viewBox="0 0 12 12"><rect x="1" y="4" width="10" height="6" rx="1"/><rect x="3" y="1" width="6" height="3"/></svg>415 208 7739</li>
    <li><svg viewBox="0 0 12 12"><path d="M1 2.5h10v7H1z M1 2.5l5 4 5-4" stroke="#fff" stroke-width=".8"/></svg>hello@kestrelmedia.co</li>
    <li><svg viewBox="0 0 12 12"><circle cx="6" cy="6" r="5.5"/></svg>www.kestrelmedia.co</li>
  </ul>

  <address class="address">2140 Alder Court<br>Juneau, Alaska 99801</address>

  <div class="person">
    <div class="person__name">TOMAS WYLANDER</div>
    <div class="person__role">CEO/FOUNDER</div>
  </div>
</section>

<section class="card card--back" aria-label="Business card, back">
  <div class="back-brand">
    <div class="wordmark"><span class="wordmark__square"></span>Kestrel Media</div>
    <div class="tagline">Online Marketing Services</div>
  </div>

  <div class="social-row">
    <span class="social-row__rule"></span>
    <div class="social-row__dots">
      <span class="social-dot"></span>
      <span class="social-dot"></span>
      <span class="social-dot"></span>
      <span class="social-dot"></span>
      <span class="social-dot"></span>
    </div>
    <span class="social-row__rule"></span>
  </div>
</section>

</body>
</html>
```